Dream Enhancing Device - Comfortable & Sweet

Hello,

We want a website that SCREAMS comfort, dream, night, sweetness...

Something that, when you look at it, feels good.

Our website is about a device that helps you make you do beautiful dreams.

So, on the landing page, one must see the a picture of the device (see attached), with description, and everything must look profesional and comfortable

Be creative.

Need :
Landing page (home)
Product page (images with descriptions)
Contact page

Sans Serif

3276b5
0392cd
33a6d7
ffffff
f68d4d
b7a5cd
876aae

• Must look comfortable, feel like something sweet
• You can use clouds, moons, stars, anythings, be creative...

```html
<!DOCTYPE html>
<html lang="en">
<head>
<meta charset="utf-8">
<title>Moonhaven – Sleep Wristbands</title>
<link rel="stylesheet" href="https://fonts.googleapis.com/css2?family=Poppins:wght@300;400;500;600;700&display=swap">
<style>
:root{
  --blue:#0a7fcf;
  --blue-band:#0a7acb;
  --ink:#1d1d1f;
  --text:#4a4a4a;
  --muted:#8a8a8a;
  --soft-bg:#f1f2f6;
  --footer:#232323;
  --footer-text:#e6e6e6;
  --copy-bg:#ececec;
  --white:#ffffff;
  --logo-tab:#0d1620;
}
*{box-sizing:border-box;margin:0;padding:0}
html,body{width:1200px;height:2782px;overflow:hidden}
body{font-family:"Poppins",sans-serif;color:var(--ink);background:var(--white);position:relative}
.abs{position:absolute}

/* header */
.site-header{position:absolute;left:0;top:0;width:1200px;height:89px;background:var(--white);z-index:3}
.search{position:absolute;left:148px;top:14px;width:201px;height:24px;border-bottom:1px solid #999}
.nav a{position:absolute;top:52px;font-size:13px;font-weight:500;color:#333;text-decoration:none;letter-spacing:.3px}
.shop-link{position:absolute;left:979px;top:12px;font-size:12px;font-weight:600;color:#333}
.cart{position:absolute;left:1026px;top:10px}
.cart-count{position:absolute;left:1037px;top:9px;width:12px;height:12px;border-radius:50%;background:var(--blue);color:#fff;font-size:8px;text-align:center;line-height:12px}
.logo-tab{position:absolute;left:514px;top:0;width:174px;height:140px;background:var(--logo-tab);border-radius:0 0 48px 48px;border:3px solid #2a6aa0;border-top:none;z-index:4;display:flex;align-items:flex-end;justify-content:center;padding-bottom:42px}
.brand-name{font-family:"Poppins",sans-serif;font-weight:600;font-size:17px;letter-spacing:.5px;color:#fff}

/* hero */
.hero{position:absolute;left:0;top:89px;width:1200px;height:556px;background:linear-gradient(90deg,#fbfbfb 0%,#f4f0ee 35%,#e8d8cc 60%,#d9c3b3 80%,#cdb9ad 100%)}
.hero h1{position:absolute;left:148px;top:196px;font-size:50px;line-height:60px;font-weight:400;color:#111}
.hero h1 b{font-weight:600}
.btn-outline{position:absolute;left:148px;top:405px;width:145px;height:40px;border:2px solid #333;border-radius:4px;font-size:14px;font-weight:500;letter-spacing:1px;color:var(--blue);display:flex;align-items:center;justify-content:center;background:rgba(255,255,255,.6)}
.hero-band-small{position:absolute;left:148px;top:110px;width:32px;height:70px;border-radius:14px;background:linear-gradient(#3a3a3a,#2f8f3a)}
.hero-bands{position:absolute;left:946px;top:495px;width:148px;height:130px;border-radius:30px;background:linear-gradient(120deg,#3fa84a,#2a2a2a 60%,#5cc05d)}

/* section headings */
.sec-mark{position:absolute;width:26px;height:26px;border-radius:50%;background:var(--blue);left:587px}
.sec-title{position:absolute;left:0;width:1200px;text-align:center;font-weight:600;letter-spacing:.5px}

/* products */
.card{position:absolute;top:829px;width:214px;height:260px;border:1px solid #ececec;border-radius:4px;background:#fff;overflow:hidden;text-align:center}
.card .shot{position:absolute;left:30px;top:70px;width:154px;height:100px;border-radius:40px;background:linear-gradient(180deg,#5a5a5a,#1f1f1f)}
.card .ribbon{position:absolute;right:-26px;top:12px;width:100px;height:20px;background:var(--blue);color:#fff;font-size:9px;font-weight:600;line-height:20px;transform:rotate(45deg);text-align:center}
.card h3{position:absolute;left:0;top:166px;width:100%;font-size:14px;font-weight:600;letter-spacing:.4px}
.card p{position:absolute;left:0;top:190px;width:100%;font-size:11px;color:var(--muted)}
.card .price{position:absolute;left:0;top:209px;width:100%;font-size:18px;color:var(--blue);font-weight:500}
.arrow-btn{position:absolute;top:943px;width:34px;height:32px;border:1.5px solid #333;border-radius:3px;display:flex;align-items:center;justify-content:center}

/* newsletter */
.newsletter{position:absolute;left:0;top:1152px;width:1200px;height:365px;background:radial-gradient(circle at 50% 85%,#2b94db 0%,var(--blue-band) 40%)}
.newsletter h2{position:absolute;top:117px;left:0;width:1200px;text-align:center;color:#fff;font-size:32px;font-weight:600;letter-spacing:.5px}
.newsletter .lead{position:absolute;top:165px;left:0;width:1200px;text-align:center;color:#e9f3fb;font-size:13px}
.newsletter .rule{position:absolute;top:197px;left:573px;width:54px;height:2px;background:#fff}
.subscribe-form{position:absolute;left:297px;top:241px;width:605px;height:46px;background:#fff;border-radius:3px;box-shadow:0 2px 6px rgba(0,0,0,.15)}
.subscribe-form .placeholder{position:absolute;left:40px;top:14px;font-size:12px;color:#aaa}
.subscribe-form .mail{position:absolute;left:18px;top:17px}
.subscribe-form .btn{position:absolute;right:5px;top:5px;width:117px;height:36px;background:#4a4a4a;color:#fff;font-size:12px;font-weight:600;display:flex;align-items:center;justify-content:center;border-radius:2px}

/* why choose */
.why-art{position:absolute;left:241px;top:1586px;width:251px;height:343px;border-radius:110px/160px;background:linear-gradient(135deg,#3a3a3a 0%,#1e1e1e 55%,#8ebfd3 100%)}
.why-title{position:absolute;left:586px;top:1572px;font-size:30px;font-weight:600}
.why-intro{position:absolute;left:586px;top:1622px;width:400px;font-size:11.5px;line-height:21px;color:var(--text)}
.feature{position:absolute;left:588px;width:420px;height:66px}
.feature .icon{position:absolute;left:0;top:0;width:66px;height:66px;border-radius:50%;background:var(--blue);display:flex;align-items:center;justify-content:center}
.feature h4{position:absolute;left:83px;top:0;font-size:16px;font-weight:600;letter-spacing:.5px}
.feature p{position:absolute;left:83px;top:26px;width:300px;font-size:11.5px;line-height:21px;color:var(--text)}

/* testimonials */
.testimonials{position:absolute;left:0;top:2029px;width:1200px;height:457px;background:var(--soft-bg)}
.quote-mark{position:absolute;left:572px;top:158px;font-size:90px;line-height:90px;color:#a9a9a9;font-weight:700;font-family:"Poppins",sans-serif}
.testimonials .body{position:absolute;left:195px;top:219px;width:810px;text-align:center;font-size:13.5px;line-height:25px;color:#555}
.person{position:absolute;top:324px;width:240px;height:80px}
.person .avatar{position:absolute;left:0;top:0;width:80px;height:80px;border-radius:50%;background:linear-gradient(#d4b8a4,#8c6b58);border:3px solid #fff}
.person .name{position:absolute;left:101px;top:20px;font-size:13px;font-weight:600;color:#888;letter-spacing:.4px}
.person .role{position:absolute;left:101px;top:43px;font-size:12.5px;color:#999}

/* footer */
.site-footer{position:absolute;left:0;top:2486px;width:1200px;height:259px;background:var(--footer);color:var(--footer-text)}
.site-footer h5{position:absolute;top:24px;font-size:17px;font-weight:400;color:var(--blue)}
.footer-brand{position:absolute;left:148px;top:160px;font-size:25px;font-weight:600;color:#fff;letter-spacing:.5px}
.footer-list{position:absolute;top:73px;list-style:none;font-size:12px;line-height:24px}
.contact-row{position:absolute;left:679px;font-size:12px;display:flex;align-items:center;gap:12px}
.social{position:absolute;left:963px;width:18px;height:18px;border:1px solid #ddd;transform:rotate(45deg)}
.copyright{position:absolute;left:0;top:2745px;width:1200px;height:37px;background:var(--copy-bg);text-align:center;font-size:11px;line-height:37px;color:#333}
</style>
</head>
<body>

<header class="site-header">
  <div class="search">
    <svg width="14" height="14" viewBox="0 0 14 14"><circle cx="6" cy="6" r="4.5" fill="none" stroke="#111" stroke-width="2"/><line x1="9.5" y1="9.5" x2="13" y2="13" stroke="#111" stroke-width="2"/></svg>
  </div>
  <nav class="nav">
    <a style="left:148px">HOME</a>
    <a style="left:241px">ABOUT US</a>
    <a style="left:358px">PRODUCTS</a>
    <a style="left:738px">SERVICES</a>
    <a style="left:848px">TESTIMONIALS</a>
    <a style="left:992px">CONTACT</a>
  </nav>
  <span class="shop-link">SHOP</span>
  <svg class="cart" width="16" height="18" viewBox="0 0 16 18"><path d="M2 6h12l-1 11H3z" fill="none" stroke="#333" stroke-width="1.5"/><path d="M5 6V4a3 3 0 0 1 6 0v2" fill="none" stroke="#333" stroke-width="1.5"/></svg>
  <span class="cart-count">0</span>
</header>
<div class="logo-tab"><span class="brand-name">MOONHAVEN</span></div>

<section class="hero">
  <div role="img" aria-label="Photo of a woman sleeping peacefully on a white pillow" class="abs" style="inset:0"></div>
  <div class="hero-band-small" role="img" aria-label="Green and black sleep wristband"></div>
  <h1><b>Lorem Ipsum is</b><br>simply dummy<br><b>text of the printing</b></h1>
  <div class="btn-outline">SHOP NOW</div>
  <div class="hero-bands" role="img" aria-label="Three green sleep wristbands"></div>
</section>

<span class="sec-mark" style="top:707px"></span>
<h2 class="sec-title" style="top:736px;font-size:37px">OUR PRODUCTS</h2>

<div class="arrow-btn" style="left:76px"><svg width="10" height="12"><path d="M7 1L2 6l5 5" fill="none" stroke="#333" stroke-width="1.5"/></svg></div>
<div class="arrow-btn" style="left:1089px"><svg width="10" height="12"><path d="M3 1l5 5-5 5" fill="none" stroke="#333" stroke-width="1.5"/></svg></div>

<article class="card" style="left:148px"><div class="shot" role="img" aria-label="Black wristband, closed" style="height:60px;top:90px"></div><span class="ribbon">NEW</span><h3>WRISTBAND-06-CLOSED</h3><p>It is a long established face</p><div class="price">$ 96.95</div></article>
<article class="card" style="left:378px"><div class="shot" role="img" aria-label="Black and grey wristband, size one"></div><span class="ribbon">NEW</span><h3>WRISTBAND-08-SIZE-01</h3><p>It is a long established face</p><div class="price">$ 96.95</div></article>
<article class="card" style="left:608px"><div class="shot" role="img" aria-label="Black and grey wristband, size three"></div><span class="ribbon">NEW</span><h3>WRISTBAND-08-SIZE-03</h3><p>It is a long established face</p><div class="price">$ 96.95</div></article>
<article class="card" style="left:838px"><div class="shot" role="img" aria-label="Black and light blue wristband, closed" style="left:62px;width:90px;background:linear-gradient(135deg,#2b2b2b,#7fb6cc)"></div><span class="ribbon">NEW</span><h3>WRISTBAND-06-CLOSED</h3><p>It is a long established face</p><div class="price">$ 96.95</div></article>

<section class="newsletter">
  <span class="sec-mark" style="top:80px;background:#fff"></span>
  <h2>SUBSCRIBE TO OUR NEWSLETTER</h2>
  <p class="lead">Sing up with your email address to receive news and updates</p>
  <span class="rule"></span>
  <div class="subscribe-form">
    <svg class="mail" width="13" height="10" viewBox="0 0 13 10"><rect width="13" height="10" fill="#bbb"/><path d="M0 0l6.5 5L13 0" fill="none" stroke="#fff"/></svg>
    <span class="placeholder">Enter your Email..</span>
    <span class="btn">SUBSCRIBE</span>
  </div>
</section>

<section>
  <div class="why-art" role="img" aria-label="Black wristband with light blue inner lining"></div>
  <h2 class="why-title">WHY CHOOSE US</h2>
  <p class="why-intro">Lorem Ipsum is simply dummy text of the printing and typesetting industry. Lorem Ipsum has been the industry's standard dummy text ever since the 1500s.</p>
  <div class="feature" style="top:1707px"><div class="icon"><svg width="30" height="30"><rect x="5" y="9" width="20" height="14" rx="3" fill="none" stroke="#fff" stroke-width="2"/></svg></div><h4>COMFORT</h4><p>Ipsum is simply dummy text of the printing and industry. Lorem Ipsum has been</p></div>
  <div class="feature" style="top:1803px"><div class="icon"><svg width="30" height="30"><circle cx="15" cy="15" r="10" fill="none" stroke="#fff" stroke-width="2"/></svg></div><h4>DREAM</h4><p>Ipsum is simply dummy text of the printing and industry. Lorem Ipsum has been</p></div>
  <div class="feature" style="top:1900px"><div class="icon"><svg width="30" height="30"><path d="M4 12h22a11 11 0 0 1-22 0z" fill="none" stroke="#fff" stroke-width="2"/></svg></div><h4>SWEETNESS</h4><p>Ipsum is simply dummy text of the printing and industry. Lorem Ipsum has been</p></div>
</section>

<section class="testimonials">
  <span class="sec-mark" style="top:58px"></span>
  <h2 class="sec-title" style="top:88px;font-size:28px">TESTIMONIALS</h2>
  <span class="quote-mark">&ldquo;</span>
  <p class="body">There are many variations of passages of Lorem Ipsum available, but the majority have suffered alteration in some form, by injected humour, or randomised words which don't look even slightly believable. If you are going to use a passage of Lorem Ipsum, you need to be sure there isn't anything embarrassing hidden in the</p>
  <div class="person" style="left:222px"><div class="avatar" role="img" aria-label="Portrait of customer"></div><span class="name">CORINNE P</span><span class="role">Lorem Ipsum simply</span></div>
  <div class="person" style="left:485px"><div class="avatar" role="img" aria-label="Portrait of customer"></div><span class="name" style="color:#333">TALIA M</span><span class="role">Lorem Ipsum simply</span></div>
  <div class="person" style="left:748px"><div class="avatar" role="img" aria-label="Portrait of customer"></div><span class="name">NORA K</span><span class="role">Lorem Ipsum simply</span></div>
</section>

<footer class="site-footer">
  <h5 style="left:148px">Contact</h5>
  <h5 style="left:397px">Explore</h5>
  <h5 style="left:555px">Links</h5>
  <h5 style="left:679px">Contact Info</h5>
  <h5 style="left:959px">Join Us On</h5>
  <span class="footer-brand">MOONHAVEN</span>
  <ul class="footer-list" style="left:397px"><li>Home</li><li>Shop</li><li>Products</li><li>Testimonials</li><li>Sign Up</li></ul>
  <ul class="footer-list" style="left:555px"><li>About</li><li>Contact Us</li><li>Services</li><li>Sing Up</li></ul>
  <div class="contact-row" style="top:76px"><svg width="10" height="13"><path d="M5 13C1 8 0 6 0 5a5 5 0 0 1 10 0c0 1-1 3-5 8z" fill="#fff"/><circle cx="5" cy="5" r="2" fill="#232323"/></svg>214 Willow Lantern Lane, Brookvale</div>
  <div class="contact-row" style="top:105px"><svg width="12" height="12"><path d="M2 0l3 3-1.5 2a8 8 0 0 0 3.5 3.5L9 7l3 3-2 2C5 12 0 7 0 2z" fill="#fff"/></svg>+1-410-555-0187</div>
  <div class="contact-row" style="top:133px"><svg width="12" height="9"><rect width="12" height="9" fill="#fff"/><path d="M0 0l6 5 6-5" fill="none" stroke="#232323"/></svg>hello@moonhaven-mail.com</div>
  <span class="social" style="top:92px"></span>
  <span class="social" style="top:122px"></span>
  <span class="social" style="top:152px"></span>
  <span class="social" style="top:182px"></span>
</footer>
<div class="copyright">@Copyright 2019</div>

</body>
</html>
```